Fun, Clean Business Card For Family Focused Travel Agency

I need a business card using specific colors and fonts as in the uploaded files. Ideally, I would like a large image of the logo on the back and all the contact info on the front. Maybe the stars/dots somewhere in a flowy form.

I do want it the contact information to be clear and easy to read. I don't want it to look too busy. Maybe even a bit minimalist.

I plan or ordering the ROUNDED CORNER business cards from Cardwell Press, so please consider that in your design.

Target Market(s)

Families with children, couples, groups of friends

Contact Information for Business Card

Marla Quent, Owner
Marla@TidewayTrips.example
Cell Phone Number 555-218-6034
Office Phone Number 555-647-1295
Specializing in Fablecrest destinations, Goldmere Parkside Resort, Cruises and All-Inclusive Vacations.

Nice but not required:
www.TidewayTrips.example
Facebook, Instagram, Twitter icons with username: TidewayTrips

Font styles to use
Sans Serif

Requirements
Must have
• Please try to use the colors from the logo as much as possible. I understand lighter shades/colors may be needed for some things.
Should not have
• NO SERIF FONTS. That is really the only thing I do not want at all

```html
<!DOCTYPE html>
<html lang="en">
<head>
<meta charset="utf-8">
<title>Tideway Trips — Business Card</title>
<link rel="stylesheet" href="https://fonts.googleapis.com/css2?family=Kaushan+Script&family=Arimo:wght@400;500&display=swap">
<style>
  :root {
    --gold: #e0b935;
    --navy: #141726;
    --blue: #1d6fb8;
    --orange: #ef7a23;
    --teal: #17ab95;
    --sky: #1b9fd6;
    --white: #ffffff;
    --ink: #1a1a1a;
    --frame: #4f8fb0;
  }
  * { box-sizing: border-box; margin: 0; padding: 0; }
  html, body { width: 1000px; height: 1200px; overflow: hidden; background: var(--white); }
  .canvas { position: relative; width: 1000px; height: 1200px; }

  .card {
    position: absolute; left: 165px; width: 662px; height: 428px;
    border-radius: 70px; background: var(--gold); overflow: hidden;
  }
  .card-front { top: 125px; }
  .card-back { top: 635px; }

  .trail { position: absolute; left: 0; top: 0; }

  .brand-small {
    position: absolute; left: 345px; top: 58px;
    display: flex; align-items: center; gap: 14px;
  }
  .brand-dot { width: 62px; height: 62px; border-radius: 50%; background: var(--navy); flex: none; }
  .brand-name {
    font-family: "Kaushan Script", sans-serif; color: var(--navy);
    font-size: 36px; line-height: 1; white-space: nowrap;
  }

  .person { position: absolute; left: 35px; top: 172px; }
  .person-name {
    font-family: "Kaushan Script", sans-serif; color: var(--blue);
    font-size: 38px; line-height: 1; font-weight: 400;
  }
  .person-role {
    font-family: "Arimo", sans-serif; color: var(--blue);
    font-size: 21px; margin: 2px 0 0 8px;
  }

  .contacts { position: absolute; left: 35px; top: 258px; list-style: none; }
  .contacts li {
    display: flex; align-items: center; gap: 8px; height: 32.5px;
    font-family: "Arimo", sans-serif; font-weight: 500; color: var(--white); font-size: 17px; letter-spacing: 0.4px;
  }
  .contacts svg { width: 20px; height: 20px; flex: none; }

  .rule { position: absolute; left: 22px; right: 24px; top: 390px; height: 1px; background: var(--orange); }
  .specialty {
    position: absolute; left: 0; right: 0; top: 396px; text-align: center;
    font-family: "Arimo", sans-serif; font-size: 12.5px; color: var(--ink);
  }

  .back-panel {
    position: absolute; left: 0; right: 0; top: 65px; height: 296px;
    background: var(--white); border: 1.5px solid var(--frame);
  }
  .brand-large {
    position: absolute; left: 70px; top: 60px;
    display: flex; align-items: center; gap: 40px;
  }
  .brand-large .brand-dot { width: 160px; height: 160px; }
  .brand-large .brand-name { font-size: 84px; line-height: 0.95; }
</style>
</head>
<body>
<main class="canvas">

  <section class="card card-front" aria-label="Card front">
    <svg class="trail" width="662" height="428" role="img" aria-label="Flowing trail of stars and dots">
      <defs>
        <linearGradient id="trailTone" x1="0" y1="0" x2="1" y2="1">
          <stop offset="0" stop-color="#ef7a23" stop-opacity="0.35"/>
          <stop offset="0.5" stop-color="#17ab95" stop-opacity="0.3"/>
          <stop offset="1" stop-color="#1b9fd6" stop-opacity="0.35"/>
        </linearGradient>
      </defs>
      <path d="M55 55 C150 80 260 120 330 160 C380 190 420 250 555 350 L545 375 C400 280 360 215 310 185 C240 145 140 110 55 85 Z" fill="url(#trailTone)"/>
    </svg>

    <div class="brand-small">
      <span class="brand-dot"></span>
      <span class="brand-name">Tideway Trips</span>
    </div>

    <div class="person">
      <h1 class="person-name">Marla Quent</h1>
      <p class="person-role">Owner</p>
    </div>

    <ul class="contacts">
      <li>
        <svg viewBox="0 0 20 20" aria-hidden="true"><rect x="5" y="1" width="10" height="18" rx="2" fill="var(--orange)"/><rect x="7" y="4" width="6" height="7" fill="var(--gold)"/><circle cx="10" cy="15" r="1.3" fill="var(--gold)"/></svg>
        555-218-6034
      </li>
      <li>
        <svg viewBox="0 0 20 20" aria-hidden="true"><path d="M4 2 L7.5 2 L9 6 L7 7.8 C8 10.5 9.5 12 12.2 13 L14 11 L18 12.5 L18 16 C18 17 17 18 16 18 C8 17.5 2.5 12 2 4 C2 3 3 2 4 2 Z" fill="var(--orange)"/></svg>
        555-647-1295
      </li>
      <li>
        <svg viewBox="0 0 20 20" aria-hidden="true"><rect x="1.5" y="4" width="17" height="12" fill="none" stroke="var(--orange)" stroke-width="1.6"/><path d="M1.5 4 L10 11 L18.5 4" fill="none" stroke="var(--orange)" stroke-width="1.6"/></svg>
        Marla@TidewayTrips.example
      </li>
      <li>
        <svg viewBox="0 0 20 20" aria-hidden="true"><g fill="none" stroke="var(--orange)" stroke-width="1.5"><circle cx="10" cy="10" r="8"/><ellipse cx="10" cy="10" rx="3.5" ry="8"/><path d="M2 10 H18 M3.5 6 H16.5 M3.5 14 H16.5"/></g></svg>
        www.TidewayTrips.example
      </li>
    </ul>

    <div class="rule"></div>
    <p class="specialty">Specializing in Fablecrest destinations, Goldmere Parkside Resort, Cruises and All-Inclusive Vacations.</p>
  </section>

  <section class="card card-back" aria-label="Card back">
    <div class="back-panel">
      <div class="brand-large">
        <span class="brand-dot"></span>
        <span class="brand-name">Tideway<br>Trips</span>
      </div>
    </div>
  </section>

</main>
</body>
</html>
```